Chorefinch/Jobwillow Style Site Design

I need a website similar to jobwillow or chorefinch, the marketing target is for Australian people. Please play with these 2 sites first if you are serious about the project.
I don't have very specific requirement, the functionalities should be like the reference site, but with different & unique design. What I want is a clean, elegant user interface with web2.0 modern style, especially homepage (When I implement your design into actual website, there will be much jquery & ajax modern technique used.)
I need design for the following pages:
1. homepage
2. login page
3. Sign up page
4. browse task page
5. post a task & confirmation page
6. Payment page
7. User Dashboard page
8. Single task page
The features must have photos of friendly looking helpers.
You can also check http://www.beta.errandmoth.example/ for reference. Be as creative & freshness as much as you can!
Target Market(s)
Australian people aging from 15 - 70.
Industry/Entity Type
Marketing
Look and feel
Each slider illustrates characteristics of the customer's brand and the style your logo design should communicate.

```html
<!DOCTYPE html>
<html lang="en">
<head>
<meta charset="utf-8">
<title>Errandly – Find people to help you</title>
<link rel="stylesheet" href="https://fonts.googleapis.com/css2?family=Titillium+Web:wght@400;600;700&family=Oswald:wght@500&family=Share+Tech+Mono&family=Roboto:wght@300;400&display=swap">
<style>
:root{
  --ink:#222;
  --dark:#2b2c2e;
  --dark-2:#404144;
  --blue:#2a8be0;
  --blue-deep:#1565b8;
  --blue-light:#5db4f2;
  --orange:#ef7a12;
  --grey-panel:#dcdcdc;
  --card:#f1f1f1;
  --text-soft:#7a7a7a;
  --white:#fff;
}
*{box-sizing:border-box;margin:0;padding:0}
html,body{width:1200px;height:1070px;overflow:hidden;background:var(--white)}
body{font-family:"Titillium Web",sans-serif;color:var(--ink)}
.page{position:relative;width:1200px;height:1070px;overflow:hidden}
.abs{position:absolute}

/* header */
.topbar{left:0;top:0;width:1200px;height:45px;background:linear-gradient(#3d3e41,#1f2022)}
.brand{display:flex;align-items:center;gap:6px;color:var(--white);font-family:"Titillium Web",sans-serif;font-weight:600;font-size:27px;line-height:1}
.brand-dot{width:12px;height:12px;border-radius:50%;background:var(--blue-light)}
.topbar .brand{left:189px;top:7px}
.mainnav{left:364px;top:13px;display:flex;gap:0;color:#eee;font-size:15px;letter-spacing:.3px}
.mainnav span{padding:0 14px;border-left:1px solid #888;line-height:17px}
.mainnav span:first-child{padding-left:0;border-left:0}
.account{left:940px;top:13px;font-size:11px;color:#ddd}

/* join band */
.joinband{left:0;top:45px;width:1200px;height:60px;background:linear-gradient(#5ab6f3,#1e86d8)}
.join-text{left:193px;top:63px;font-family:"Share Tech Mono",monospace;font-size:15px;color:#13314f}
.btn-social{left:407px;top:51px;width:224px;height:43px;background:linear-gradient(#3f6fb8,#2b549a);border:1px solid #1d3f78;display:flex;align-items:center}
.btn-social .mark{width:36px;height:100%;background:#244a88;border-right:1px solid #5a85c8}
.btn-social span,.btn-email span{flex:1;text-align:center;color:var(--white);font-family:"Oswald",sans-serif;font-size:15px;letter-spacing:.2px}
.or{left:643px;top:64px;font-size:15px;color:#143a63}
.btn-email{left:674px;top:51px;width:241px;height:43px;background:linear-gradient(#f58c22,#e06a08);border:1px solid #b9570a;display:flex;align-items:center}
.btn-email .mark{width:52px;height:100%;display:flex;align-items:center;justify-content:center;border-right:1px solid #f6a55a}

/* hero */
.hero{left:0;top:105px;width:1200px;height:412px;background:linear-gradient(90deg,#f4f4f4 0%,#b9b9b9 20%,#8a8a8a 50%,#b0b0b0 80%,#f2f2f2 100%)}
.hero-photos{position:absolute;inset:0;background:
  linear-gradient(180deg,rgba(255,255,255,.25),rgba(255,255,255,0) 40%,rgba(255,255,255,.25)),
  linear-gradient(90deg,rgba(255,255,255,.6),rgba(255,255,255,0) 18%,rgba(255,255,255,0) 82%,rgba(255,255,255,.6))}
.headline-1{left:273px;top:189px;width:674px;height:81px;background:rgba(255,255,255,.88);display:flex;align-items:center;justify-content:center;font-family:"Oswald",sans-serif;font-size:56px;letter-spacing:-1px;color:#111}
.headline-2{left:189px;top:273px;width:841px;height:78px;background:linear-gradient(#4cb2f2,#1f86dc);display:flex;align-items:center;justify-content:center;font-family:"Oswald",sans-serif;font-size:60px;letter-spacing:-1px;color:#0d0d0d}
.slide-prev,.slide-next{top:266px;width:80px;height:92px;color:var(--white);font-family:"Oswald",sans-serif;font-size:13px;display:flex;align-items:center;gap:6px}
.slide-prev{left:0;background:#0b0b0b;clip-path:polygon(0 0,68% 0,100% 50%,68% 100%,0 100%);padding-left:10px}
.slide-next{left:1120px;background:#0b0b0b;clip-path:polygon(32% 0,100% 0,100% 100%,32% 100%,0 50%);justify-content:flex-end;padding-right:10px}
.stats{left:442px;top:439px;width:334px;height:78px;background:#0c0c0c;color:var(--white);font-family:"Share Tech Mono",monospace;font-size:15px;text-align:center;line-height:24px;padding-top:5px}
.stats-cta{left:476px;top:491px;width:255px;height:24px;background:linear-gradient(#3aa0ec,#1c78cf);color:var(--white);font-family:"Roboto",sans-serif;font-size:12px;font-weight:400;display:flex;align-items:center;justify-content:center;letter-spacing:.2px}

/* search */
.searchband{left:0;top:517px;width:1200px;height:93px;background:linear-gradient(#3c3d40,#27282a)}
.search-badge{left:187px;top:528px;width:70px;height:70px;border-radius:50%;background:var(--blue);display:flex;align-items:center;justify-content:center}
.search-input{left:287px;top:542px;width:444px;height:43px;background:linear-gradient(#fafafa,#e8e8e8);border:2px solid #cfcfcf;font-family:"Roboto",sans-serif;font-weight:300;font-size:13px;color:#666;padding:13px 34px}
.search-btn{left:739px;top:542px;width:118px;height:43px;background:linear-gradient(#2b8fe3,#1566bd);border:1px solid #0f4f95;color:var(--white);font-family:"Oswald",sans-serif;font-size:20px;display:flex;align-items:center;justify-content:center}
.social{display:flex;gap:9px}
.social i{display:block;width:15px;height:15px;border-radius:50%;background:var(--blue)}
.searchband-social{left:880px;top:556px}

/* partners */
.partners{left:0;top:610px;width:1200px;height:73px;background:linear-gradient(#f5f5f5,#dedede);border-bottom:1px solid #ccc}
.partner-arrow{top:615px}
.partner{top:630px;background:#b9b9b9;border-radius:4px}

/* content */
.panel{left:188px;top:699px;width:781px;height:295px}
.panel .scallop{position:absolute;background-repeat:repeat}
.panel .top{left:0;top:0;right:0;height:16px;background:radial-gradient(circle,var(--grey-panel) 8px,transparent 8.5px) 0 0/18px 16px repeat-x}
.panel .bottom{left:0;bottom:0;right:0;height:16px;background:radial-gradient(circle,var(--grey-panel) 8px,transparent 8.5px) 0 0/18px 16px repeat-x}
.panel .left{left:0;top:0;bottom:0;width:16px;background:radial-gradient(circle,var(--grey-panel) 8px,transparent 8.5px) 0 0/16px 18px repeat-y}
.panel .right{right:0;top:0;bottom:0;width:16px;background:radial-gradient(circle,var(--grey-panel) 8px,transparent 8.5px) 0 0/16px 18px repeat-y}
.panel .fill{position:absolute;left:8px;top:8px;right:8px;bottom:8px;background:var(--grey-panel)}
.card{top:720px;height:253px;background:var(--card);border-radius:6px;box-shadow:0 0 2px rgba(0,0,0,.08)}
.card h2{position:absolute;font-family:"Titillium Web",sans-serif;font-weight:600;font-size:27px;letter-spacing:-.5px;line-height:1}
.card p{position:absolute;font-family:"Roboto",sans-serif;font-size:11px;line-height:13.8px;color:var(--text-soft)}
.btn-more{position:absolute;height:18px;padding:0 9px;background:linear-gradient(#2d8fe2,#1766be);color:var(--white);font-family:"Roboto",sans-serif;font-size:10.5px;line-height:18px;box-shadow:0 1px 1px rgba(0,0,0,.3)}
.rule{position:absolute;height:1px;background:#d6d6d6}
.date{position:absolute;width:37px;height:34px;background:linear-gradient(#2f94e6,#1766be);color:var(--white);text-align:center;font-family:"Roboto",sans-serif;line-height:1}
.date b{display:block;font-size:18px;font-weight:400;margin-top:2px}
.date small{display:block;font-size:10px;margin-top:1px}

/* footer */
.footer{left:0;top:1011px;width:1200px;height:59px;background:linear-gradient(#3a3b3e,#222325)}
.footer-links{left:192px;top:1019px;font-size:11px;color:#eee}
.footer-links span{padding:0 5px;border-left:1px solid #aaa}
.footer-links span:first-child{padding-left:0;border-left:0}
.copyright{left:192px;top:1043px;font-size:11px;color:#eee}
.footer-social{left:533px;top:1028px}
.footer .brand{left:887px;top:14px;font-size:26px}
</style>
</head>
<body>
<div class="page">

  <header class="abs topbar">
    <div class="abs brand"><i class="brand-dot"></i>Errandly</div>
    <nav class="abs mainnav"><span>BROWSE TASKS</span><span>BECOME A RUNNER</span><span>POST A TASK</span><span>HOW IT WORKS</span></nav>
    <div class="abs account">Sign up &nbsp;|&nbsp; Login</div>
  </header>

  <section class="abs joinband"></section>
  <div class="abs join-text">Join Errandly Today!</div>
  <div class="abs btn-social"><i class="mark"></i><span>CONNECT WITH FRIENDNET</span></div>
  <div class="abs or">OR</div>
  <div class="abs btn-email">
    <i class="mark"><svg width="30" height="20" viewBox="0 0 30 20"><rect x="1" y="1" width="28" height="18" rx="2" fill="#fff"/><path d="M2 3 L15 12 L28 3" fill="none" stroke="#e57412" stroke-width="3"/></svg></i>
    <span>SIGN UP WITH YOUR EMAIL</span>
  </div>

  <section class="abs hero">
    <div class="hero-photos" role="img" aria-label="Grid of black and white photos of friendly helpers, office workers and city buildings, with a few blue tiles"></div>
  </section>
  <h1 class="abs headline-1">FIND PEOPLE TO HELP YOU</h1>
  <div class="abs headline-2">AROUND THE HOME AND OFFICE</div>
  <div class="abs slide-prev"><svg width="10" height="16" viewBox="0 0 10 16"><path d="M8 2 L2 8 L8 14" fill="none" stroke="#fff" stroke-width="2.5"/></svg>PREV</div>
  <div class="abs slide-next">NEXT<svg width="10" height="16" viewBox="0 0 10 16"><path d="M2 2 L8 8 L2 14" fill="none" stroke="#fff" stroke-width="2.5"/></svg></div>
  <div class="abs stats">Over 72,000 people across Australia<br>&amp; over $1650,000 of jobs created.</div>
  <div class="abs stats-cta">It's FREE to post a task, get started here</div>

  <section class="abs searchband"></section>
  <div class="abs search-badge">
    <svg width="44" height="44" viewBox="0 0 44 44"><circle cx="22" cy="22" r="17" fill="none" stroke="#fff" stroke-width="3"/><path d="M22 11 V22 L15 27" fill="none" stroke="#fff" stroke-width="3" stroke-linecap="round"/></svg>
  </div>
  <div class="abs search-input">Type Keywords here to search online jobs</div>
  <div class="abs search-btn">SEARCH</div>
  <div class="abs social searchband-social"><i></i><i></i><i></i><i></i><i></i></div>

  <section class="abs partners"></section>
  <svg class="abs partner-arrow" style="left:152px" width="26" height="64" viewBox="0 0 26 64"><path d="M22 2 L4 32 L22 62" fill="none" stroke="#333" stroke-width="3"/></svg>
  <svg class="abs partner-arrow" style="left:1010px" width="26" height="64" viewBox="0 0 26 64"><path d="M4 2 L22 32 L4 62" fill="none" stroke="#333" stroke-width="3"/></svg>
  <div class="abs partner" style="left:191px;width:132px;height:32px;top:630px"></div>
  <div class="abs partner" style="left:343px;width:36px;height:48px;top:623px;border-radius:50%"></div>
  <div class="abs partner" style="left:407px;width:48px;height:48px;top:623px"></div>
  <div class="abs partner" style="left:474px;width:164px;height:24px;top:635px"></div>
  <div class="abs partner" style="left:660px;width:70px;height:30px;top:630px"></div>
  <div class="abs partner" style="left:750px;width:64px;height:56px;top:618px"></div>
  <div class="abs partner" style="left:831px;width:52px;height:56px;top:618px"></div>
  <div class="abs partner" style="left:905px;width:94px;height:36px;top:628px"></div>

  <section class="abs panel">
    <div class="scallop top"></div><div class="scallop bottom"></div><div class="scallop left"></div><div class="scallop right"></div>
    <div class="fill"></div>
  </section>

  <article class="abs card" style="left:213px;width:234px">
    <h2 style="left:20px;top:10px">WELCOME</h2>
    <p style="left:18px;top:48px;width:210px">Lorem ipsum dolor sit amet, consectetuer adipiscing elit, sed diam nonummy nibh euismod tincidunt ut laoreet dolore magna aliquam erat volutpat. Ut wisi enim ad minim veniam, quis nostrud exerci tation ullamcorper suscipit lobortis nisl ut aliquip ex ea commodo consequat. Duis autem vel eum iriure dolor in hendrerit in vulputate velit esse molestie consequat, vel illum dolore eu feugiat nulla facilisis at vero eros et accumsan ..</p>
    <span class="btn-more" style="left:18px;top:220px">Read More</span>
  </article>

  <article class="abs card" style="left:465px;width:234px">
    <h2 style="left:18px;top:8px;color:#666">REGENT PROJECTS</h2>
    <p style="left:18px;top:46px;width:205px">Lorem ipsum dolor sit amet, consectetuer adipiscing elit, sed diam nonummy nibh euismod tincidunt ut</p>
    <span class="btn-more" style="left:16px;top:96px">Read More</span>
    <div class="rule" style="left:16px;top:133px;width:200px"></div>
    <p style="left:16px;top:144px;width:210px">Lorem ipsum dolor sit amet, consectetuer adipiscing elit, sed diam nonummy nibh euismod tincidunt ut Lorem ipsum dolor sit amet, consectetuer adipiscing elit.</p>
    <span class="btn-more" style="left:16px;top:211px">Read More</span>
  </article>

  <article class="abs card" style="left:716px;width:234px">
    <h2 style="left:18px;top:8px">EVENTS &amp; NEWS</h2>
    <div class="date" style="left:20px;top:48px"><b>17</b><small>JAN</small></div>
    <p style="left:65px;top:45px;width:160px">Lorem ipsum dolor sit amet, consectetuer adipiscing elit, sed diam nonummy nibh euismod tincidunt ut laoreet dolore .</p>
    <div class="rule" style="left:18px;top:119px;width:196px"></div>
    <div class="date" style="left:20px;top:135px"><b>15</b><small>JAN</small></div>
    <p style="left:65px;top:132px;width:160px">Lorem ipsum dolor sit amet, consectetuer adipiscing elit, sed diam nonummy nibh euismod tincidunt ut laoreet dolore magna aliquam erat volutpat.</p>
    <span class="btn-more" style="left:16px;top:219px">View all events</span>
  </article>

  <footer class="abs footer">
    <div class="abs brand"><i class="brand-dot"></i>Errandly</div>
  </footer>
  <div class="abs footer-links"><span>About</span><span>Careers</span><span>Blog</span><span>Tech City</span><span>Directory API</span></div>
  <div class="abs copyright">© 2013 | Errandly All rights reserved</div>
  <div class="abs social footer-social"><i></i><i></i><i></i><i></i><i></i></div>

</div>
</body>
</html>
```